Lumora Works - Design & Marketing Website Re-branding

UPDATE:
We are working on finalizing our color palette but are hoping that the designers will guide us to the right choice of colors by looking at our color inspiration file that we just uploaded and lead us in the right direction.

-----

I am exploring new design inspiration for a re-branding of my website. My current website is old and outdated and I lack the time to design it myself in addition to the fact that I am my own worst client.

I do website design, development and marketing as well as some SEO consulting and business development for small to mid-size companies in a range of industries.

https://lumoraworks.example

I like clean modern designs without cartoon images. The brands I'm going after are looking for a professional look and feel. I need something that shows my many years of being in business that is very professional.

I prefer minimal use of color. Mostly black and white with maybe one or two other colors. I am open to the suggestions by the designer.

Target Market(s)

Small to mid-size companies

Industry/Entity Type

Website Design, SEO and Markeitng

Number of Pages Required

4 page

Font styles to use
Sans Serif

Requirements
Must have
• Must be clean, modern and professional - I am not a huge fan of a lot of color and I'm open to new color suggestions by the designer
Nice to have
• A good balance of whitespace to content and graphics
Should not have
• Please no people illustrations

```html
<!DOCTYPE html>
<html lang="en">
<head>
<meta charset="utf-8">
<title>Lumora Works</title>
<link href="https://fonts.googleapis.com/css2?family=Inter:wght@400;500;600;700;800&display=swap" rel="stylesheet">
<style>
:root{
  --ink:#000;
  --paper:#fff;
  --soft:#f5f5f5;
  --pill:#1f1f1f;
  --stage-top:#000;
  --stage-bottom:#3a3a3a;
}
*{box-sizing:border-box;margin:0;padding:0}
html,body{width:1200px;height:1200px;overflow:hidden}
body{background:linear-gradient(180deg,var(--stage-top) 0%,#1e1e1e 45%,var(--stage-bottom) 100%);font-family:'Inter',sans-serif;color:var(--ink)}
.stage{position:absolute;left:0;top:0;width:1932px;height:1932px;transform:scale(0.62112);transform-origin:0 0}
.page{position:absolute;left:637px;top:9px;width:658px;height:1913px;background:var(--paper);overflow:hidden}
.abs{position:absolute}
.brand{font-weight:800;font-size:15px;letter-spacing:-.3px;display:flex;align-items:center;gap:4px;white-space:nowrap}
.brand .dot{width:6px;height:6px;border-radius:50%;background:currentColor}
.nav{display:flex;align-items:center;gap:13px;background:var(--pill);border-radius:13px;height:25px;padding:0 8px;color:#fff;font-size:8.5px;letter-spacing:.2px;white-space:nowrap}
.nav .home{width:22px;height:17px;border-radius:9px;background:#555;display:flex;align-items:center;justify-content:center}
.btn-dark{background:var(--pill);color:#fff;font-weight:700;font-size:8.5px;border-radius:13px;display:flex;align-items:center;justify-content:center;gap:4px}
.hero-title{left:0;width:658px;top:108px;text-align:center;font-size:34px;line-height:40px;font-weight:800;letter-spacing:.3px}
.hero-sub{left:0;width:658px;top:196px;text-align:center;font-size:12.5px}
.hero-btn{left:260px;top:244px;width:138px;height:31px;border:2px solid var(--ink);border-radius:16px;font-weight:800;font-size:12px;display:flex;align-items:center;justify-content:center;letter-spacing:.4px}
.trust-line{left:24px;top:347px;width:610px;height:1.5px;background:var(--ink)}
.trust-label{left:24px;top:350px;width:76px;height:19px;background:var(--ink);color:#fff;font-size:12.5px;font-weight:500;padding-left:5px;line-height:19px}
.clients{left:24px;top:380px;width:610px;display:flex;justify-content:space-between;align-items:center;height:24px}
.client{font-size:12.5px;font-weight:700;color:#333;display:flex;align-items:center;gap:5px}
.client .mark{width:17px;height:17px;border-radius:50%;background:#bbb}
.card{border-radius:10px}
.simplified{left:20px;top:496px;width:618px;height:146px;background:var(--ink);color:#fff;overflow:hidden}
.simplified .shot{position:absolute;left:370px;top:0;width:248px;height:146px;background:radial-gradient(ellipse at 65% 55%,#4a3a52 0%,#262129 40%,#0a0a0a 80%)}
.simplified h2{position:absolute;left:12px;top:60px;font-size:16.5px;font-weight:400}
.simplified p{position:absolute;left:12px;top:88px;width:240px;font-size:12.5px;line-height:15px}
.btn-light{background:#fff;color:var(--ink);font-weight:700;font-size:8.5px;border-radius:10px;display:flex;align-items:center;justify-content:center;gap:5px}
.service{top:673px;width:297px;height:137px;background:var(--soft)}
.service .icon{position:absolute;left:20px;top:20px}
.service h3{position:absolute;left:91px;top:22px;font-size:16.5px;font-weight:400}
.service p{position:absolute;left:91px;top:49px;width:196px;font-size:12.5px;line-height:15px}
.service .go{position:absolute;left:107px;top:107px;width:83px;height:18px;background:var(--ink);color:#fff;border-radius:9px;font-size:8.5px;font-weight:700;display:flex;align-items:center;justify-content:center;gap:4px}
b{font-weight:700}
.quote{left:20px;top:841px;width:618px;height:146px;background:var(--ink);color:#fff;text-align:center}
.quote p{position:absolute;left:110px;width:398px;top:26px;font-size:16.5px;line-height:20px}
.quote cite{position:absolute;left:0;width:618px;top:101px;font-style:normal;font-size:12.5px}
.inspire-title{left:20px;top:1069px;font-size:24px;line-height:30px;font-weight:400}
.inspire-copy{left:216px;top:1069px;width:424px;font-size:12.5px;line-height:15px}
.points{left:173px;top:1191px;width:460px}
.point{position:relative;height:70px}
.point .coin{position:absolute;left:0;top:0;width:27px;height:27px;border-radius:50%;background:var(--ink);color:#fff;font-size:15px;font-weight:500;display:flex;align-items:center;justify-content:center}
.point h4{position:absolute;left:43px;top:-1px;font-size:12.5px;font-weight:700}
.point p{position:absolute;left:43px;top:22px;width:400px;font-size:12.5px;line-height:15px}
.cta{left:20px;top:1467px;width:618px;height:181px;border-radius:20px;background:linear-gradient(180deg,#000 0%,#111 30%,#5a5a5a 75%,#444 100%);color:#fff;text-align:center}
.cta h2{position:absolute;left:0;width:618px;top:36px;font-size:33px;font-weight:800;letter-spacing:.2px}
.cta p{position:absolute;left:0;width:618px;top:83px;font-size:12.5px}
.cta .go{position:absolute;left:266px;top:120px;width:86px;height:26px;border-radius:13px;background:#fff;color:var(--ink);font-weight:700;font-size:8.5px;display:flex;align-items:center;justify-content:center;letter-spacing:.3px}
.footer{left:0;top:1731px;width:658px;height:182px;background:var(--ink);color:#fff}
.footer .nav{box-shadow:0 0 14px rgba(255,255,255,.12)}
.social{display:flex;gap:13px}
.social span{width:13px;height:13px;border-radius:50%;background:#fff;display:block}
.rule{left:0;top:152px;width:658px;height:1px;background:#777}
.legal{top:162px;font-size:8.5px;color:#ddd}
</style>
</head>
<body>
<div class="stage">
<div class="page">

  <header>
    <div class="abs brand" style="left:20px;top:20px">Lumora Works<span class="dot"></span></div>
    <nav class="abs nav" style="left:166px;top:16px;width:326px">
      <span class="home"><svg width="11" height="10" viewBox="0 0 11 10"><path d="M1 5 5.5 1 10 5M2.5 4v5h6V4" fill="none" stroke="#fff" stroke-width="1.4"/></svg></span>
      <span>SIMPLIFY</span><span>DESIGN</span><span>CARE</span><span>INSPIRE</span><span>ABOUT</span><span>COLLABORATE</span>
    </nav>
    <a class="abs btn-dark" style="left:579px;top:16px;width:59px;height:25px">CONNECT</a>
  </header>

  <section class="hero">
    <h1 class="abs hero-title">EVERY BUSINESS HAS A STORY.<br>WE HELP YOU TELL IT.</h1>
    <p class="abs hero-sub">Compelling website experiences that elevate your business.</p>
    <a class="abs hero-btn">LETS CHAT!</a>
  </section>

  <section class="trusted">
    <div class="abs trust-line"></div>
    <div class="abs trust-label">Trusted by:</div>
    <div class="abs clients">
      <span class="client"><span class="mark"></span>Keystead</span>
      <span class="client">Harbor Table</span>
      <span class="client">Northline</span>
      <span class="client">Brightpath</span>
      <span class="client">Snapwise</span>
    </div>
  </section>

  <section class="abs card simplified">
    <div class="shot" role="img" aria-label="Angled screenshot of a subscription website with growth chart"></div>
    <h2>WEBSITE <b>SIMPLIFIED</b></h2>
    <p>A complete end-to-end website subscription solution that propels your business forward.</p>
    <a class="abs btn-light" style="left:462px;top:115px;width:144px;height:19px">Complete Website Solution
      <svg width="9" height="9" viewBox="0 0 10 10"><path d="M1 5h7M5 1.5 8.5 5 5 8.5" stroke="#000" stroke-width="2" fill="none"/></svg></a>
  </section>

  <section class="abs card service" style="left:20px">
    <svg class="icon" width="44" height="44" viewBox="0 0 44 44"><rect x="2" y="6" width="28" height="22" rx="4"/><path d="M19 14v16l-4-3-2 3 7 10h14l3-11-11-3v-12z" fill="#fff" stroke="#000" stroke-width="2.5" stroke-linejoin="round"/></svg>
    <h3>CUSTOM <b>WEBSITE</b></h3>
    <p>Blending the best principles of design, data and functionality to express your brand.</p>
    <a class="go">Website Care <svg width="8" height="8" viewBox="0 0 10 10"><path d="M1 5h7M5 1.5 8.5 5 5 8.5" stroke="#fff" stroke-width="2" fill="none"/></svg></a>
  </section>
  <section class="abs card service" style="left:341px">
    <svg class="icon" width="44" height="44" viewBox="0 0 44 44"><circle cx="22" cy="22" r="21"/><circle cx="22" cy="16" r="6" fill="#fff"/><path d="M14 40V27a8 8 0 0 1 16 0v13" fill="#fff"/><rect x="21" y="28" width="3" height="13" fill="#000"/></svg>
    <h3>WEBSITE <b>SUPPORT</b></h3>
    <p>Reliable top tier managed website support, maintenance and hosting.</p>
    <a class="go">Website Care <svg width="8" height="8" viewBox="0 0 10 10"><path d="M1 5h7M5 1.5 8.5 5 5 8.5" stroke="#fff" stroke-width="2" fill="none"/></svg></a>
  </section>

  <section class="abs card quote">
    <p>Lumora Works provided us with a <b>high quality, functional, easy to navigate</b> and <b>beautiful</b> website.</p>
    <cite>- R. Daley</cite>
  </section>

  <section class="inspire">
    <h2 class="abs inspire-title">WE CREATE<br>WEBSITES<br>THAT <b>INSPIRE</b></h2>
    <p class="abs inspire-copy">We are a collaborative team of word nerds, choreographers of shapes &amp; ideas, ambassadors of data, content warriors and inspirational conversationalists ready to help you no matter where you are in your journey.</p>
    <div class="abs points">
      <div class="point"><span class="coin">$</span><h4>Proven process</h4><p>We have carefully crafted each step in our process for successful outcomes.</p></div>
      <div class="point"><span class="coin">$</span><h4>Connection</h4><p>We take the time to truly listen and understand your audience and business needs.</p></div>
      <div class="point"><span class="coin">$</span><h4>Exceeding your goals</h4><p>We develop actionable strategies for success based on your unique goals.</p></div>
    </div>
  </section>

  <section class="abs cta">
    <h2>LET'S WORK TOGETHER</h2>
    <p>Let's have a conversation to discuss your needs and how we can help.</p>
    <a class="go">GET STARTED</a>
  </section>

  <footer class="abs footer">
    <div class="abs brand" style="left:20px;top:28px">Lumora Works<span class="dot"></span></div>
    <nav class="abs nav" style="left:146px;top:25px;width:326px">
      <span class="home"><svg width="11" height="10" viewBox="0 0 11 10"><path d="M1 5 5.5 1 10 5M2.5 4v5h6V4" fill="none" stroke="#fff" stroke-width="1.4"/></svg></span>
      <span>SIMPLIFY</span><span>DESIGN</span><span>CARE</span><span>INSPIRE</span><span>ABOUT</span><span>COLLABORATE</span>
    </nav>
    <div class="abs social" style="left:551px;top:23px"><span></span><span></span><span></span></div>
    <a class="abs btn-light" style="left:540px;top:50px;width:98px;height:20px">
      <svg width="15" height="11" viewBox="0 0 15 11"><rect x="1" y="1" width="9" height="6" rx="2" fill="none" stroke="#000" stroke-width="1.3"/><rect x="5" y="4" width="9" height="6" rx="2" fill="#fff" stroke="#000" stroke-width="1.3"/></svg>LETS CHAT!</a>
    <div class="abs rule"></div>
    <p class="abs legal" style="left:20px">© 2024 Lumora Works, LLC. All Rights Reserved.</p>
    <p class="abs legal" style="left:520px;display:flex;gap:14px"><span>Privacy</span><span>Terms</span><span>Disclaimer</span></p>
  </footer>

</div>
</div>
</body>
</html>
```